Washroom Services - Flyer Design - to compete with international players

I need a flyer to compete with large international suppliers like Corvane Services who dominate the washroom services market here in New Zealand. Washroom services include supply and replenishment of air fresheners, soaps, sanitisers, hand towels, toilet paper and sanitary disposal units.
Looking at A4 brochure folded to DLE size (ie in 3) recommendations please if another orientation/size would be better.
Target Market(s)
Businesses with multiple washrooms in one site such as office blocks/towers, municiple buildings, restaurants, gyms.
Requirements
Must have
- Quillary Washrooms Logo, images of the dispensers - nb any other logo currently on a dispenser needs the Quillary Washrooms logo photo shopped onto it.
Nice to have
- Icons to represent different product offerings
Should not have
- Any images of people

```html
<!DOCTYPE html>
<html lang="en">
<head>
<meta charset="utf-8">
<title>Quillary Washrooms – Washroom Services Trifold</title>
<link href="https://fonts.googleapis.com/css2?family=Open+Sans:ital,wght@0,400;0,600;0,700;1,400;1,600&family=Roboto+Condensed:wght@300;400;700&family=Roboto:wght@300;400;700;900&display=swap" rel="stylesheet">
<style>
  :root{
    --navy:#253a5e;
    --blue:#1a7fc8;
    --sky:#2f9ad8;
    --ink:#2b2b2b;
    --text:#333;
    --paper:#ffffff;
    --stage:#e8edf0;
  }
  *{box-sizing:border-box;margin:0;padding:0}
  html,body{width:1200px;height:1200px;overflow:hidden}
  body{background:var(--stage);font-family:"Open Sans",sans-serif;color:var(--text)}
  .canvas{position:relative;width:1200px;height:1200px}
  .trifold{position:absolute;left:45px;top:207px;display:flex;box-shadow:0 10px 30px rgba(0,0,0,.15)}
  .panel{position:relative;width:370px;height:786px;background:var(--paper);overflow:hidden}
  .panel + .panel{border-left:1px solid #e2e6ea}
  .footer-band{position:absolute;left:0;right:0;bottom:0;height:30px;background:var(--navy)}

  /* Services panel */
  .section-bar{position:absolute;left:0;right:0;background:var(--navy);color:#fff;
    font-family:"Roboto Condensed",sans-serif;font-size:25px;display:flex;align-items:center;justify-content:center;letter-spacing:.2px}
  .section-bar b{font-weight:700}
  .section-bar span{font-weight:300;margin-left:6px}
  .italic-copy{position:absolute;left:28px;right:26px;font-size:11px;font-style:italic;line-height:1.32;text-align:justify}
  .italic-copy p + p{margin-top:6px}
  .italic-copy .accent{color:var(--blue);font-weight:600}
  .photo-slot{position:absolute}
  .round-photo{position:absolute;border-radius:50%;border:5px solid var(--blue);overflow:hidden;box-shadow:0 4px 8px rgba(0,0,0,.2)}

  /* Contact panel */
  .contact-heading{position:absolute;left:0;right:0;top:36px;text-align:center;color:var(--blue);
    font-family:"Roboto",sans-serif;font-weight:700;font-size:19px}
  .contact-copy{position:absolute;left:30px;right:30px;top:74px;font-size:11.3px;font-weight:700;line-height:1.3;text-align:center;color:#222}
  .pleasure{position:absolute;left:0;right:0;top:178px;text-align:center;color:var(--blue);
    font-family:"Roboto Condensed",sans-serif;font-weight:700;font-size:19.5px;line-height:1.3}
  .rule{position:absolute;left:0;right:0;height:5px;background:var(--blue)}

  /* Company name block */
  .brand{position:absolute;display:flex;align-items:center;gap:10px}
  .brand-dot{flex:none;border-radius:50%;background:var(--blue)}
  .brand-name{color:var(--navy);font-family:"Open Sans",sans-serif;font-weight:700;white-space:nowrap;line-height:1.1}
  .brand-sub{display:block;color:var(--text);font-family:"Open Sans",sans-serif;font-weight:400;white-space:nowrap;margin-top:2px}

  .contact-card{position:absolute;left:0;right:0;top:628px;text-align:center}
  .contact-name{color:var(--blue);font-weight:700;font-size:16.5px}
  .contact-role{color:#111;font-weight:600;font-size:16px;margin-top:2px}
  .contact-lines{display:inline-block;text-align:left;margin-top:8px;font-size:12.5px;color:#222;line-height:1.5}
  .contact-lines div{display:flex;align-items:center;gap:10px}
  .contact-lines svg{width:10px;height:10px;flex:none}

  /* Cover panel */
  .headline-small{position:absolute;left:30px;top:500px;color:var(--sky);font-family:"Roboto",sans-serif;font-weight:900;font-size:35px;letter-spacing:.5px}
  .headline-large{position:absolute;left:26px;top:534px;color:var(--ink);font-family:"Roboto",sans-serif;font-weight:400;font-size:94px;letter-spacing:-1px;line-height:1}
  .intro-box{position:absolute;left:24px;right:24px;top:650px;height:92px;background:var(--sky);border-radius:12px;
    color:#fff;font-weight:700;font-size:12px;line-height:1.35;text-align:center;padding:10px 18px;display:flex;flex-direction:column;justify-content:center;gap:6px;
    box-shadow:0 0 0 3px #dbe9f4}
</style>
</head>
<body>
<div class="canvas">
  <div class="trifold">

    <!-- Panel: services -->
    <section class="panel panel-services">
      <div class="section-bar" style="top:22px;height:50px"><b>WASHROOM</b><span>DISPENSERS</span></div>
      <div class="italic-copy" style="top:94px">
        <p>We have a wide range of stylish quality dispensers that are all provided to you on a <span class="accent">“free on-loan”</span> basis.</p>
        <p>We will arrange a site visit to go over your specific requirements to ensure the dispensers provided are fit for purpose as well as complementing the washroom facility.</p>
        <p>Our team of professional installers provide installation of all units and dispensers to appropriate specifications for optimal user experience and safety.</p>
      </div>
      <div class="photo-slot" role="img" aria-label="Row of white washroom dispensers: sanitary bins, soap, air freshener and towel units"
           style="left:40px;right:30px;top:242px;height:102px;background:linear-gradient(180deg,#f4f5f6,#dcdfe2);border-radius:6px"></div>
      <div class="section-bar" style="top:364px;height:44px"><b>PAPER</b><span>PRODUCTS</span></div>
      <div class="round-photo" role="img" aria-label="Stack of white toilet paper rolls and hand towels"
           style="left:113px;top:420px;width:145px;height:145px;background:radial-gradient(circle,#ffffff 30%,#e3e6e9 100%)"></div>
      <div class="italic-copy" style="top:580px">
        <p>Paper products (toilet paper and hand towels) for your washroom come in a huge variety and will be a large component of your washroom inventory.</p>
        <p>We will work with you to understand who your washroom visitors are and the best types of products to suit their needs and your budget.</p>
        <p>If you need to have different products in different washrooms or switch between products you can. We have a flexible approach to your paper product needs.</p>
      </div>
      <div class="footer-band"></div>
    </section>

    <!-- Panel: contact -->
    <section class="panel panel-contact">
      <h2 class="contact-heading">Contact Us to Find out More</h2>
      <p class="contact-copy">Whether you’re just starting out, doing a refurbishment or know it’s time for a new washroom services supplier, contact us. We will come to you to discuss your specific requirements and come back to you with a quote, installation and service plan.</p>
      <p class="pleasure">It’s our pleasure to make your<br>washroom users’ experience pleasant.</p>
      <div class="rule" style="top:268px"></div>
      <div class="photo-slot" role="img" aria-label="Gloved cleaning of a chrome tap with a yellow cloth and blue spray bottle"
           style="left:0;right:0;top:280px;height:255px;background:linear-gradient(120deg,#35b7d8 0%,#9fdcef 35%,#e9eef2 60%,#c5ccd3 100%)"></div>
      <div class="rule" style="top:541px"></div>
      <div class="brand" style="left:70px;top:566px">
        <span class="brand-dot" style="width:20px;height:20px"></span>
        <div>
          <span class="brand-name" style="font-size:21px">Quillary Washrooms</span>
          <span class="brand-sub" style="font-size:11px">Washroom Services</span>
        </div>
      </div>
      <div class="contact-card">
        <div class="contact-name">Tessa Marlowe</div>
        <div class="contact-role">Director</div>
        <div class="contact-lines">
          <div><svg viewBox="0 0 10 10"><path d="M2 0.8 3.6 2.6 2.8 3.6C3.4 5 4.8 6.4 6.3 7.1L7.3 6.3 9.2 8 8.2 9.4C4.5 9 1 5.4 0.6 1.8Z" fill="var(--blue)"/></svg>021 555 0184 / 09 555 0137</div>
          <div><svg viewBox="0 0 10 10"><circle cx="5" cy="5" r="4.3" fill="none" stroke="var(--blue)" stroke-width="1.2"/><path d="M0.8 5H9.2M5 0.8C3 3 3 7 5 9.2M5 0.8C7 3 7 7 5 9.2" fill="none" stroke="var(--blue)" stroke-width=".8"/></svg>www.quillarywashrooms.co.nz</div>
        </div>
      </div>
      <div class="footer-band" style="height:36px"></div>
    </section>

    <!-- Panel: cover -->
    <section class="panel panel-cover">
      <div class="brand" style="left:30px;top:40px">
        <span class="brand-dot" style="width:26px;height:26px"></span>
        <div>
          <span class="brand-name" style="font-size:26px">Quillary Washrooms</span>
          <span class="brand-sub" style="font-size:13px">Washroom Services</span>
        </div>
      </div>
      <div class="rule" style="top:130px"></div>
      <div class="photo-slot" role="img" aria-label="Bright public washroom with lilac cubicle doors, urinals, basin and colourful panels"
           style="left:0;right:0;top:141px;height:262px;background:linear-gradient(90deg,#7fb2e6 0%,#b8a6e3 40%,#c7b7ec 70%,#9cc4ea 100%)"></div>
      <div class="round-photo" role="img" aria-label="Washroom with dark cubicle door and row of basins"
           style="left:110px;top:335px;width:152px;height:152px;background:linear-gradient(160deg,#5d6a7a,#a8b3bf 60%,#d9dde2)"></div>
      <div class="headline-small">PROFESSIONAL</div>
      <div class="headline-large">CLEAN</div>
      <div class="intro-box">
        <p>Quillary Washrooms are a locally owned professional washroom services company.</p>
        <p>We work with you to provide the best washroom solution for your business and the people who use your bathrooms.</p>
      </div>
      <div class="footer-band" style="height:28px"></div>
    </section>

  </div>
</div>
</body>
</html>
```